Card for Real Estate Developer

We need a business card design for a Real Estate Development company based in Texas. We focus on retail, apartment and residential development. Our target is predominantly investors looking to us to place their money properly to achieve a significant return. On the other side we sell our services to large retailers as their preferred developer assisting them in locating, building and leasing their real estate.

Target Market(s)

Investors

Industry/Entity Type

Real Estate Development

Contact Information for Business Card

Would like to stay within the company color scheme, while keeping the design moderately simple.

Font styles to use
Other font styles liked:
• per attached document

Requirements
Must have
• Name
• Phone
• Email
• Website
• Logo Prominently Displayed
• Stay within the colors provided in the attached document

```html
<!DOCTYPE html>
<html lang="en">
<head>
<meta charset="utf-8">
<title>Halvern Development – Business Card</title>
<link href="https://fonts.googleapis.com/css2?family=Cinzel:wght@400;600&family=Open+Sans:wght@400;600&display=swap" rel="stylesheet">
<style>
  :root {
    --backdrop: #3a3230;
    --card: #111113;
    --card-edge: #1c1c1f;
    --accent: #7fb6dc;
    --ink: #e8ecef;
    --ink-soft: #c9d0d6;
  }
  * { margin: 0; padding: 0; box-sizing: border-box; }
  html, body { width: 1200px; height: 814px; overflow: hidden; }
  body {
    background: var(--backdrop);
    font-family: "Open Sans", Arial, sans-serif;
    position: relative;
  }
  .card {
    position: absolute;
    top: 258px;
    width: 520px;
    height: 298px;
    background: var(--card);
    border: 1px solid var(--card-edge);
    box-shadow: 0 18px 40px rgba(0,0,0,0.45);
  }
  .card--front { left: 50px; }
  .card--back  { left: 630px; }

  /* front */
  .brand {
    position: absolute;
    left: 40px;
    top: 112px;
    width: 200px;
    text-align: center;
  }
  .brand__mark {
    display: block;
    width: 26px;
    height: 26px;
    margin: 0 auto 14px;
    background: var(--accent);
  }
  .brand__name {
    font-family: "Cinzel", Georgia, serif;
    font-weight: 400;
    color: var(--ink);
    font-size: 25px;
    line-height: 1.15;
    letter-spacing: 1px;
  }
  .contact {
    position: absolute;
    left: 268px;
    top: 62px;
  }
  .contact__name {
    font-family: "Cinzel", Georgia, serif;
    color: var(--accent);
    font-size: 19px;
    letter-spacing: 0.5px;
  }
  .contact__role {
    font-family: "Cinzel", Georgia, serif;
    color: var(--ink-soft);
    font-size: 12px;
    margin-bottom: 8px;
  }
  .contact__address {
    color: var(--ink);
    font-size: 12px;
    line-height: 1.4;
    margin-bottom: 4px;
  }
  .contact__list { list-style: none; }
  .contact__item {
    display: flex;
    align-items: center;
    gap: 8px;
    color: var(--ink);
    font-size: 12px;
    line-height: 19px;
  }
  .contact__icon { width: 11px; height: 11px; flex: none; }
  .contact__icon * { fill: var(--accent); }

  /* back */
  .back-brand {
    position: absolute;
    left: 0; right: 0;
    top: 104px;
    text-align: center;
  }
  .back-brand__mark {
    display: block;
    width: 30px; height: 30px;
    margin: 0 auto 16px;
    background: var(--accent);
  }
  .back-brand__name {
    font-family: "Cinzel", Georgia, serif;
    color: var(--ink);
    font-size: 30px;
    letter-spacing: 2px;
  }
  .back-web {
    position: absolute;
    left: 0; right: 0;
    top: 216px;
    text-align: center;
    color: var(--ink);
    font-size: 12px;
    letter-spacing: 4px;
  }
</style>
</head>
<body>

<section class="card card--front" aria-label="Business card front">
  <div class="brand">
    <span class="brand__mark"></span>
    <p class="brand__name">Halvern Development</p>
  </div>

  <div class="contact">
    <h1 class="contact__name">Daniel Reyes</h1>
    <p class="contact__role">CEO/Founder</p>
    <p class="contact__address">2140 Cedar Ridge Drive<br>Austin, Texas 78701</p>
    <ul class="contact__list">
      <li class="contact__item">
        <svg class="contact__icon" viewBox="0 0 12 12"><path d="M2.5 0.5 L4.5 0.5 L5.2 3.2 L3.8 4.3 C4.5 5.9 6.1 7.5 7.7 8.2 L8.8 6.8 L11.5 7.5 L11.5 9.5 C11.5 10.6 10.6 11.5 9.5 11.5 C4.5 11.5 0.5 7.5 0.5 2.5 C0.5 1.4 1.4 0.5 2.5 0.5 Z"/></svg>
        512 555 0147
      </li>
      <li class="contact__item">
        <svg class="contact__icon" viewBox="0 0 12 12"><path d="M3 0 H9 A1 1 0 0 1 10 1 V11 A1 1 0 0 1 9 12 H3 A1 1 0 0 1 2 11 V1 A1 1 0 0 1 3 0 Z M3.5 1.5 V9 H8.5 V1.5 Z"/></svg>
        512 555 0183
      </li>
      <li class="contact__item">
        <svg class="contact__icon" viewBox="0 0 12 12"><path d="M3 0 H8 V3 H3 Z M0.5 4 H11.5 V10 H0.5 Z M3 8 H9 V12 H3 Z"/></svg>
        512 555 0129
      </li>
      <li class="contact__item">
        <svg class="contact__icon" viewBox="0 0 12 12"><path d="M0.5 2 H11.5 V10 H0.5 Z M1.5 3 L6 6.5 L10.5 3 Z" fill-rule="evenodd"/></svg>
        info@halverndev.com
      </li>
      <li class="contact__item">
        <svg class="contact__icon" viewBox="0 0 12 12"><circle cx="6" cy="6" r="5.5"/></svg>
        www.halverndev.com
      </li>
    </ul>
  </div>
</section>

<section class="card card--back" aria-label="Business card back">
  <div class="back-brand">
    <span class="back-brand__mark"></span>
    <p class="back-brand__name">Halvern</p>
  </div>
  <p class="back-web">www.halverndev.com</p>
</section>

</body>
</html>
```